Your 'not so average' farmers. We are farmers and entrepreneurs trying to connect the great divide.

KTB (Brosmere Holdings Inc) is a family owned farm (in our 3rd generation). We grow vegetables (corn, soy, potatoes, snap beans) but we also invest in and grow businesses. These other businesses can be non-farming related businesses. We are family oriented, environmentally concise, and active in our small community. We need a business card to hand out to our fellow farmers, businesses we would like to partner with and invest in, and community members. So, we need a card with a natural, 'tenders of the land' feel for the farmers but no overly so that we seem centered on farming for the other businesses. We would like it to have our Company info (name, number, email, phone, fax) then Personal info for us five who run the joint (Name, phone, email). So we will order 100 cards for each 5 who work at KTB (500total) that is professional, not boring or hokey, but catching and unique.
Target Market(s)
Farmers, Business Owners, Investors, Community Members
Industry/Entity Type
Farming
Contact Information for Business Card
Office info on one side:
Brosmere Holdings Inc.
1187 Larkin Rd.
Pell Hollow, WI 54872
Office: (608) 555-0417
Fax: (608) 555-0283
brosmereoffice@quillpost.example
Personal Info for the 5 who run KTB. Everybody will have their own personal info on their cards(maybe on the other side):
Name
Mobile
Email
Look and feel

```html
<!DOCTYPE html>
<html lang="en">
<head>
<meta charset="utf-8">
<title>Brosmere Holdings Inc. – Business Card</title>
<link rel="stylesheet" href="https://fonts.googleapis.com/css2?family=Bitter:wght@400;600;700&display=swap">
<style>
  :root {
    --paper: #ffffff;
    --ink: #2b2b2b;
    --leaf: #5a9a4f;
    --badge: #2a2a2a;
    --badge-text: #ffffff;
    --rule: #555555;
    --edge: #9a9a9a;
    --corn-yellow: #f1e36a;
    --corn-green: #8cc152;
  }
  html, body {
    margin: 0;
    padding: 0;
    width: 1200px;
    height: 702px;
    overflow: hidden;
    background: var(--paper);
  }
  .card {
    position: relative;
    width: 1200px;
    height: 702px;
    overflow: hidden;
    background: var(--paper);
    border-left: 2px solid var(--edge);
    box-sizing: border-box;
    font-family: "Bitter", Georgia, serif;
    color: var(--ink);
  }
  .personal {
    position: absolute;
    left: 78px;
    top: 96px;
  }
  .holder-name {
    margin: 0 0 2px;
    font-size: 55px;
    font-weight: 600;
    letter-spacing: 1px;
    color: var(--leaf);
    line-height: 1.15;
  }
  .personal-line {
    margin: 0;
    font-size: 36px;
    font-weight: 400;
    line-height: 54px;
  }
  .divider {
    position: absolute;
    left: 78px;
    top: 346px;
    width: 590px;
    height: 0;
    border-top: 2px solid var(--rule);
  }
  .office {
    position: absolute;
    left: 78px;
    top: 424px;
  }
  .company-name {
    margin: 0 0 2px;
    font-size: 35px;
    font-weight: 700;
    line-height: 1.2;
  }
  .office-line {
    margin: 0;
    font-size: 31px;
    line-height: 44px;
  }
  .badge {
    position: absolute;
    left: 749px;
    top: 138px;
    width: 452px;
    height: 452px;
    border-radius: 50%;
    background: var(--badge);
    color: var(--badge-text);
    text-align: center;
  }
  .badge-icon {
    position: absolute;
    left: 218px;
    top: 18px;
    width: 46px;
    height: 90px;
  }
  .badge-title {
    position: absolute;
    left: 0;
    right: 0;
    top: 100px;
    margin: 0;
    font-size: 76px;
    font-weight: 400;
    line-height: 1.13;
  }
  .badge-crops {
    position: absolute;
    left: 0;
    right: 0;
    top: 296px;
    margin: 0;
    font-size: 27px;
    line-height: 1.33;
  }
</style>
</head>
<body>
  <div class="card">
    <section class="personal">
      <h1 class="holder-name">CARD HOLDER NAME</h1>
      <p class="personal-line">personal@quillpost.example</p>
      <p class="personal-line">333-000-000</p>
    </section>

    <div class="divider"></div>

    <section class="office">
      <h2 class="company-name">Brosmere Holdings Inc.</h2>
      <p class="office-line">1187 Larkin Rd. Pell Hollow, WI 54872</p>
      <p class="office-line">Office: (608) 555-0417 Fax: (608) 555-0283</p>
      <p class="office-line">brosmereoffice@quillpost.example</p>
    </section>

    <div class="badge">
      <svg class="badge-icon" viewBox="0 0 46 90" role="img" aria-label="Small illustration of an ear of corn in its green husk">
        <defs>
          <linearGradient id="corn-tone" x1="0" y1="0" x2="0" y2="1">
            <stop offset="0" stop-color="var(--corn-yellow)"/>
            <stop offset="0.6" stop-color="var(--corn-yellow)"/>
            <stop offset="1" stop-color="var(--corn-green)"/>
          </linearGradient>
        </defs>
        <rect x="6" y="2" width="34" height="86" rx="17" fill="url(#corn-tone)"/>
      </svg>
      <p class="badge-title">Local<br>Produce</p>
      <p class="badge-crops">corn, soy, potatoes<br>&amp; snap beans</p>
    </div>
  </div>
</body>
</html>
```